Bluestone Advisory & Mgmt - Professional Business Cards

Hi!

I am a Real Estate Developer and Construction Consultant.

I have a lot of inspiration from previous designs and would be open to using the attached Designs as a starting point. I would like to see these styles incorporated into your designs.

I really need professional business card to go with it that includes my important info.

Look forward to seeing your designs!.

Target Market(s)

My Target market are building owners, lawyers, consultants.

Industry/Entity Type

Real Estate Development

Contact Information for Business Card

My Name: Dorian Pelkey
My Title: Principle
Company Name: Bluestone Advisory & Mgmt, LLC
Address: 348 West 71st Street, 9th FL New York, NY 10023
Mobile: 917.806.3971
Website: bam-hvx.example

Font styles to use
Serif
Sans Serif

Colors

Designer to choose colors to be used in the design.

Requirements
Must have
• Must incorporate the logo attached or have new that looks similar.
• Must use professional font that will be seen and judged by wealthy land owners and developers.
• Must incorporate some of the color green.
Should not have
• Photo's or pictures of people or buildings of any kind.

```html
<!DOCTYPE html>
<html lang="en">
<head>
<meta charset="utf-8">
<title>Bluestone Advisory &amp; Mgmt - Professional Business Cards</title>
<link rel="stylesheet" href="https://fonts.googleapis.com/css2?family=Cinzel:wght@400;500&family=Raleway:wght@500;800&display=swap">
<style>
  :root {
    --page: #e9eaec;
    --card-light: #ffffff;
    --card-dark: #4c4b4d;
    --green: #3db874;
    --ghost-light: #f2f2f2;
    --ghost-dark: #555456;
    --text-light: #ffffff;
    --shadow: rgba(0, 0, 0, 0.18);
  }
  * { margin: 0; padding: 0; box-sizing: border-box; }
  html, body { width: 1200px; height: 2195px; overflow: hidden; }
  body { background: var(--page); position: relative; }

  .card {
    position: absolute;
    left: 150px;
    width: 900px;
    height: 516px;
    overflow: hidden;
    box-shadow: 0 30px 50px var(--shadow);
  }
  .card--front { top: 420px; background: var(--card-light); }
  .card--back { top: 1250px; background: var(--card-dark); }

  .ghost-name {
    position: absolute;
    left: 20px;
    bottom: -34px;
    font-family: "Raleway", sans-serif;
    font-weight: 800;
    font-size: 180px;
    line-height: 1;
    letter-spacing: -6px;
    white-space: nowrap;
  }
  .card--front .ghost-name { color: var(--ghost-light); }
  .card--back .ghost-name { color: var(--ghost-dark); }

  .brand-name {
    position: absolute;
    right: 82px;
    top: 78px;
    text-align: right;
    font-family: "Raleway", sans-serif;
    font-weight: 500;
    color: var(--green);
    font-size: 46px;
    line-height: 1.12;
  }

  .company {
    position: absolute;
    left: 50px;
    top: 58px;
    font-family: "Cinzel", serif;
    font-weight: 500;
    font-size: 38px;
    line-height: 1.05;
    text-transform: uppercase;
    color: var(--text-light);
  }
  .company__lead { color: var(--green); display: block; }

  .contact-block {
    position: absolute;
    left: 491px;
    top: 292px;
    font-family: "Cinzel", serif;
    text-transform: uppercase;
    color: var(--text-light);
  }
  .person-name { font-size: 36px; font-weight: 500; line-height: 1; letter-spacing: 0.5px; white-space: nowrap; }
  .person-title { font-size: 16px; letter-spacing: 0.5px; margin-top: 4px; }
  .contact-list { list-style: none; margin-top: 22px; font-size: 17px; line-height: 1.25; }
  .contact-list li { position: relative; padding-left: 27px; white-space: nowrap; }
  .contact-list svg { position: absolute; left: 0; top: 4px; width: 14px; height: 14px; fill: var(--text-light); }
</style>
</head>
<body>

<section class="card card--front" aria-label="Card front">
  <div class="ghost-name" aria-hidden="true">Bluestone</div>
  <div class="brand-name">Bluestone<br>Advisory &amp; Mgmt</div>
</section>

<section class="card card--back" aria-label="Card back">
  <div class="ghost-name" aria-hidden="true">Bluestone</div>
  <h1 class="company">
    <span class="company__lead">Bluestone</span>
    Advisory &amp;<br>Mgmt, LLC
  </h1>
  <div class="contact-block">
    <div class="person-name">Dorian Pelkey</div>
    <div class="person-title">Principle</div>
    <ul class="contact-list">
      <li>
        <svg viewBox="0 0 24 24" aria-hidden="true"><path d="M6.6 10.8a15.1 15.1 0 0 0 6.6 6.6l2.2-2.2c.3-.3.7-.4 1-.2 1.1.4 2.3.6 3.6.6.6 0 1 .4 1 1V20c0 .6-.4 1-1 1A17 17 0 0 1 3 4c0-.6.4-1 1-1h3.5c.6 0 1 .4 1 1 0 1.3.2 2.5.6 3.6.1.3 0 .7-.2 1z"/></svg>
        917 806 3971
      </li>
      <li>
        <svg viewBox="0 0 24 24" aria-hidden="true"><path d="M12 2a10 10 0 1 0 0 20 10 10 0 0 0 0-20zm6.9 6h-3a15.6 15.6 0 0 0-1.3-3.6A8 8 0 0 1 18.9 8zM12 4c.8 1.2 1.5 2.5 1.900 4h-3.8c.4-1.5 1.1-2.8 1.9-4zM4.3 14a8 8 0 0 1 0-4h3.4a16 16 0 0 0 0 4zm.8 2h3c.3 1.3.8 2.5 1.3 3.6A8 8 0 0 1 5.1 16zm3-8h-3a8 8 0 0 1 4.3-3.6C8.9 5.5 8.4 6.7 8.1 8zM12 20c-.8-1.2-1.5-2.5-1.9-4h3.8c-.4 1.5-1.1 2.8-1.9 4zm2.3-6H9.7a14 14 0 0 1 0-4h4.6a14 14 0 0 1 0 4zm.3 5.6c.5-1.1 1-2.3 1.3-3.6h3a8 8 0 0 1-4.3 3.6zm1.7-5.6a16 16 0 0 0 0-4h3.4a8 8 0 0 1 0 4z"/></svg>
        bam-hvx.example
      </li>
      <li>
        <svg viewBox="0 0 24 24" aria-hidden="true"><path d="M12 2a7 7 0 0 0-7 7c0 5.3 7 13 7 13s7-7.7 7-13a7 7 0 0 0-7-7zm0 9.5a2.5 2.5 0 1 1 0-5 2.5 2.5 0 0 1 0 5z"/></svg>
        348 West 71st Street, 9th FL<br>New York, NY 10023
      </li>
    </ul>
  </div>
</section>

</body>
</html>
```